Window Cleaning Flyer targeting Shopfronts and Small Commercial Work

Single page flyer similar to the flyer targeting small commercial work and shopfronts

Please include the following text:

Brisk Pane Services delivers high quality service to suburbs all around Melbourne. From Frankston to Kalkallo, Brisk has you covered!

With over 10 years experience, Brisk specialises in providing:
- Window Cleaning: via elevated work platforms, rope access and extension poles
- Pressure Cleaning: Including chlorine treatment to prevent mould regrowth on concrete area
- Roof Gutter Cleaning: using our ladder free gutter vacuum

We pride ourselves on neat and professional presentation and vast geographical reach across Melbourne.

Our services can be completed on a frequency that meets your window cleaning needs. Whether a weekly clean or a yearly service.

Brisk Pane Services Melbourne takes care of all your window cleaning needs.

Contact Us now for free quote!

Target Market(s)

Small business and commercial building owners

Industry/Entity Type

Window Cleaning

Requirements
Must have
• Only use photos/logos provided
Should not have
• Stock phots

```html
<!DOCTYPE html>
<html lang="en">
<head>
<meta charset="utf-8">
<title>Brisk Pane Services – Flyer</title>
<link href="https://fonts.googleapis.com/css2?family=Open+Sans:wght@400;600;700&family=Roboto+Slab:wght@700&family=PT+Serif:ital@1&family=Roboto:wght@900&display=swap" rel="stylesheet">
<style>
  :root{
    --blue:#1b4e86;
    --blue-dark:#153f6e;
    --yellow:#f4e200;
    --ink:#1f1f1f;
    --muted:#333;
    --page-bg:#c9c9c9;
    --paper:#ffffff;
  }
  html,body{margin:0;padding:0;overflow:hidden}
  body{width:869px;height:1200px;background:var(--page-bg);position:relative;font-family:"Open Sans",Arial,sans-serif;color:var(--ink)}
  .flyer{position:absolute;left:40px;top:36px;width:788px;height:1118px;background:var(--paper);overflow:hidden}
  .header-art{position:absolute;left:0;top:0}
  .brand{position:absolute;left:22px;top:92px;color:var(--yellow);font-family:"Roboto",Arial,sans-serif;font-weight:900}
  .brand-name{font-size:78px;line-height:1;letter-spacing:2px}
  .brand-tag{font-size:22px;letter-spacing:1px;margin-top:6px}
  .badge-text{position:absolute;left:554px;top:330px;width:192px;text-align:center;color:var(--yellow);font-family:"PT Serif",Georgia,serif;font-style:italic;line-height:1}
  .badge-text .over{font-size:28px}
  .badge-text .num{font-size:74px;margin-top:-4px}
  .badge-text .years{font-size:18px;margin-top:-2px}
  .intro{position:absolute;left:28px;top:514px;width:740px;font-size:20px;line-height:29px;margin:0;color:var(--ink)}
  .services-title{position:absolute;left:28px;top:596px;margin:0;font-size:23px;font-weight:700;color:var(--blue)}
  .service{position:absolute;display:flex;gap:10px}
  .service svg{flex:none;margin-top:4px}
  .service h3{margin:0;font-family:"Roboto Slab",Georgia,serif;font-size:19px;color:var(--ink);line-height:24px}
  .service p{margin:2px 0 0;font-family:"PT Serif",Georgia,serif;font-style:normal;font-size:14.5px;line-height:19px;color:var(--muted)}
  .svc-window{left:28px;top:646px;width:330px}
  .svc-gutter{left:422px;top:646px;width:340px}
  .svc-pressure{left:28px;top:726px;width:330px}
  .points{position:absolute;left:28px;top:816px;width:740px;margin:0;padding:0;list-style:none}
  .points li{display:flex;gap:12px;font-size:16px;line-height:22px;margin-bottom:14px;color:var(--ink)}
  .points svg{flex:none;margin-top:3px}
  .cta-lead{position:absolute;left:38px;top:990px;font-size:19px;margin:0}
  .cta-quote{position:absolute;left:38px;top:1020px;background:var(--blue);color:#fff;font-size:25px;padding:2px 10px;border-radius:3px;line-height:30px}
  .cta-quote strong{font-weight:700}
  .phone{position:absolute;left:38px;top:1066px;display:flex;align-items:center;gap:6px;color:var(--blue);font-size:36px;font-weight:700;font-family:"Open Sans",Arial,sans-serif}
  .contact-band{position:absolute;right:0;bottom:0}
  .contact-lines{position:absolute;right:16px;bottom:10px;color:#fff;font-family:"PT Serif",Georgia,serif;font-size:16px;line-height:27px;text-align:right}
  .contact-lines div{display:flex;align-items:center;justify-content:flex-end;gap:8px}
</style>
</head>
<body>
<div class="flyer">
  <svg class="header-art" width="788" height="500" viewBox="0 0 788 500" aria-hidden="false">
    <defs>
      <linearGradient id="bldg" x1="0" y1="0" x2="1" y2="1">
        <stop offset="0" stop-color="#5b5f63"/>
        <stop offset=".45" stop-color="#c8965a"/>
        <stop offset=".8" stop-color="#7a8a55"/>
        <stop offset="1" stop-color="#b9b6b2"/>
      </linearGradient>
      <linearGradient id="lift" x1="0" y1="0" x2="1" y2="1">
        <stop offset="0" stop-color="#a34a2e"/>
        <stop offset=".5" stop-color="#3d3f3d"/>
        <stop offset="1" stop-color="#7c9a62"/>
      </linearGradient>
      <clipPath id="bigClip"><circle cx="640" cy="160" r="318"/></clipPath>
    </defs>
    <path d="M0 0H788V470C600 492 300 440 0 372Z" fill="var(--blue)"/>
    <path d="M0 378C300 446 600 498 788 476V498C600 512 300 468 0 402Z" fill="#fff"/>
    <path d="M0 400C300 464 600 508 788 488" fill="none" stroke="var(--yellow)" stroke-width="5"/>
    <circle cx="640" cy="160" r="326" fill="var(--yellow)"/>
    <circle cx="640" cy="160" r="320" fill="#fff"/>
    <rect x="0" y="0" width="788" height="500" clip-path="url(#bigClip)" fill="url(#bldg)" role="img" aria-label="Photo of a worker cleaning a building facade with timber slat screens using an extension pole"/>
    <circle cx="160" cy="366" r="118" fill="var(--yellow)"/>
    <circle cx="160" cy="366" r="113" fill="#fff"/>
    <circle cx="160" cy="366" r="107" fill="url(#lift)" role="img" aria-label="Photo of an elevated work platform beside a brick building"/>
    <g transform="translate(650,402)">
      <polygon fill="var(--blue)" stroke="#fff" stroke-width="3" points="96,0 75.3,20.2 83.1,48 55.2,55.2 48,83.1 20.2,75.3 0,96 -20.2,75.3 -48,83.1 -55.2,55.2 -83.1,48 -75.3,20.2 -96,0 -75.3,-20.2 -83.1,-48 -55.2,-55.2 -48,-83.1 -20.2,-75.3 0,-96 20.2,-75.3 48,-83.1 55.2,-55.2 83.1,-48 75.3,-20.2"/>
    </g>
  </svg>

  <div class="brand">
    <div class="brand-name">BRISK</div>
    <div class="brand-tag">PANE SERVICES</div>
  </div>

  <div class="badge-text">
    <div class="over">over</div>
    <div class="num">10</div>
    <div class="years">years of<br>experience</div>
  </div>

  <p class="intro">Brisk Pane Services delivers high quality service to suburbs all around Melbourne. From Frankston to Kalkallo, Brisk has you covered!</p>

  <h2 class="services-title">Brisk specialises in providing:</h2>

  <div class="service svc-window">
    <svg width="20" height="20" viewBox="0 0 20 20"><circle cx="10" cy="10" r="8.5" fill="none" stroke="var(--blue)" stroke-width="1.5"/><rect x="7" y="6" width="6" height="8" fill="none" stroke="var(--blue)" stroke-width="1.4"/></svg>
    <div><h3>Window Cleaning</h3><p>via elevated work platforms, rope access and extension poles</p></div>
  </div>
  <div class="service svc-gutter">
    <svg width="20" height="20" viewBox="0 0 20 20"><circle cx="10" cy="10" r="8.5" fill="none" stroke="var(--blue)" stroke-width="1.5"/><path d="M6 13h8M10 5v8" stroke="var(--blue)" stroke-width="1.6"/></svg>
    <div><h3>Gutter Cleaning</h3><p>(using our ladder free gutter vacuum)</p></div>
  </div>
  <div class="service svc-pressure">
    <svg width="20" height="20" viewBox="0 0 20 20"><circle cx="10" cy="10" r="8.5" fill="none" stroke="var(--blue)" stroke-width="1.5"/><path d="M6 14L14 6" stroke="var(--blue)" stroke-width="1.6"/></svg>
    <div><h3>Pressure Washing</h3><p>Including chlorine treatment to prevent mould regrowth on concrete area</p></div>
  </div>

  <ul class="points">
    <li><svg width="14" height="20" viewBox="0 0 14 20"><path d="M9 0L1 11h5l-2 9 9-12H8z" fill="var(--blue)"/></svg><span>We pride ourselves on neat and professional presentation and vast geographical reach across Melbourne.</span></li>
    <li><svg width="14" height="20" viewBox="0 0 14 20"><path d="M9 0L1 11h5l-2 9 9-12H8z" fill="var(--blue)"/></svg><span>Our services can be completed on a frequency that meets your window cleaning needs. Whether a weekly clean or a yearly service.</span></li>
    <li><svg width="14" height="20" viewBox="0 0 14 20"><path d="M9 0L1 11h5l-2 9 9-12H8z" fill="var(--blue)"/></svg><span>Brisk Pane Services Melbourne takes care of all your window cleaning needs.</span></li>
  </ul>

  <p class="cta-lead">Contact the Brisk Team for an easy,</p>
  <div class="cta-quote">Get a <strong>FREE</strong> quote today!</div>
  <div class="phone">
    <svg width="34" height="34" viewBox="0 0 24 24"><path d="M6.6 10.8c1.4 2.8 3.8 5.1 6.6 6.6l2.2-2.2c.3-.3.7-.4 1-.2 1.1.4 2.3.6 3.6.6.6 0 1 .4 1 1V20c0 .6-.4 1-1 1C10.6 21 3 13.4 3 4c0-.6.4-1 1-1h3.5c.6 0 1 .4 1 1 0 1.3.2 2.5.6 3.6.1.3 0 .7-.2 1z" fill="var(--blue)"/></svg>
    <span>(03) 9000 4821</span>
  </div>

  <svg class="contact-band" width="400" height="66" viewBox="0 0 400 66" aria-hidden="true">
    <path d="M26 0H400V66H0Z" fill="var(--yellow)"/>
    <path d="M40 0H400V66H14Z" fill="var(--blue)"/>
  </svg>
  <div class="contact-lines">
    <div><svg width="18" height="13" viewBox="0 0 18 13"><rect x=".75" y=".75" width="16.5" height="11.5" fill="none" stroke="#fff" stroke-width="1.5"/><path d="M1 1l8 6 8-6" fill="none" stroke="#fff" stroke-width="1.5"/></svg>hello@briskpane.com.au</div>
    <div><svg width="15" height="15" viewBox="0 0 16 16"><circle cx="8" cy="8" r="7" fill="none" stroke="#fff" stroke-width="1.3"/><path d="M1 8h14M8 1c-3 3-3 11 0 14M8 1c3 3 3 11 0 14" fill="none" stroke="#fff" stroke-width="1.1"/></svg>www.briskpane-melbourne.com.au</div>
  </div>
</div>
</body>
</html>
```